Small rum distillery looking for bottle design

Small rum distillery in Estonia. Looking for bottle lable design. It should be simple but at the same time point out from the variety of other bottles.
As we are a small nordic country, design can be some how nordic or represent our country. It can also have some connection with sailing or sea as we know it pirates love it.
Bottle we are using is Corvane 540

Industry/Entity Type

food and beverage

Other font styles liked:
• Baskerville

```html
<!DOCTYPE html>
<html lang="en">
<head>
<meta charset="UTF-8">
<title>Halvik Distillery – Premium Rum Label</title>
<link rel="stylesheet" href="https://fonts.googleapis.com/css2?family=Libre+Baskerville&family=Montserrat:wght@600;700&display=swap">
<style>
  :root {
    --backdrop: #062a66;
    --backdrop-deep: #021a45;
    --label-navy: #0f1c38;
    --label-navy-light: #1c2d52;
    --gold: #d9a441;
    --gold-light: #f0c96a;
    --cream: #f4ecd8;
    --white: #ffffff;
    --orange: #e8833a;
    --crest-red: #b8323a;
  }
  * { margin: 0; padding: 0; box-sizing: border-box; }
  html, body { width: 1200px; height: 1200px; overflow: hidden; }
  body {
    background: radial-gradient(circle at 50% 50%, var(--backdrop) 0%, var(--backdrop-deep) 100%);
    position: relative;
  }
  .label {
    position: absolute;
    left: 200px;
    top: 180px;
    width: 800px;
    height: 840px;
  }
  .label-shapes { position: absolute; inset: 0; }
  .label-text {
    position: absolute;
    left: 0;
    width: 800px;
    text-align: center;
  }
  .origin-banner {
    top: 150px;
    font-family: "Montserrat", sans-serif;
    font-weight: 700;
    font-size: 20px;
    letter-spacing: 2px;
    color: var(--label-navy);
  }
  .brand-name {
    top: 318px;
    font-family: "Libre Baskerville", serif;
    font-size: 84px;
    letter-spacing: 4px;
    color: var(--white);
    line-height: 1;
  }
  .brand-sub {
    top: 432px;
    font-family: "Libre Baskerville", serif;
    font-size: 26px;
    letter-spacing: 9px;
    color: var(--white);
  }
  .established {
    top: 528px;
    font-family: "Montserrat", sans-serif;
    font-weight: 600;
    font-size: 28px;
    letter-spacing: 3px;
    color: var(--cream);
  }
  .established .dot { color: var(--orange); }
  .company-name {
    top: 600px;
    font-family: "Montserrat", sans-serif;
    font-weight: 700;
    font-size: 44px;
    letter-spacing: 2px;
    color: var(--cream);
  }
  .product-type {
    top: 684px;
    font-family: "Montserrat", sans-serif;
    font-weight: 700;
    font-size: 19px;
    letter-spacing: 1px;
    color: var(--cream);
  }
  .volume {
    top: 730px;
    font-family: "Montserrat", sans-serif;
    font-weight: 700;
    font-size: 24px;
    letter-spacing: 2px;
    color: var(--orange);
  }
</style>
</head>
<body>
  <div class="label">
    <svg class="label-shapes" viewBox="0 0 800 840" width="800" height="840" aria-hidden="false">
      <defs>
        <radialGradient id="rays-glow" cx="50%" cy="45%" r="55%">
          <stop offset="0%" stop-color="#2a3d66"/>
          <stop offset="100%" stop-color="#0f1c38"/>
        </radialGradient>
      </defs>

      <!-- ribbon tails behind the body -->
      <path class="ribbon-tail" d="M0,560 L130,560 L130,640 L0,640 L30,600 Z" fill="#0a1428" stroke="#d9a441" stroke-width="4"/>
      <path class="ribbon-tail" d="M800,560 L670,560 L670,640 L800,640 L770,600 Z" fill="#0a1428" stroke="#d9a441" stroke-width="4"/>

      <!-- label body -->
      <path class="label-body"
        d="M110,0 L690,0 A60,60 0 0 0 750,60 L750,740 A60,60 0 0 0 690,800 L110,800 A60,60 0 0 0 50,740 L50,60 A60,60 0 0 0 110,0 Z"
        fill="var(--label-navy)"/>

      <!-- sunburst area -->
      <rect x="90" y="60" width="620" height="520" rx="40" fill="url(#rays-glow)"
        role="img" aria-label="Soft sunburst rays radiating behind the name"/>

      <!-- gold inner frame -->
      <path class="label-frame"
        d="M118,20 L682,20 A52,52 0 0 0 730,68 L730,732 A52,52 0 0 0 682,780 L118,780 A52,52 0 0 0 70,732 L70,68 A52,52 0 0 0 118,20 Z"
        fill="none" stroke="var(--gold)" stroke-width="6"/>
      <path class="label-frame-thin"
        d="M126,34 L674,34 A44,44 0 0 0 716,76 L716,724 A44,44 0 0 0 674,766 L126,766 A44,44 0 0 0 84,724 L84,76 A44,44 0 0 0 126,34 Z"
        fill="none" stroke="var(--gold-light)" stroke-width="2"/>

      <!-- crown ornament -->
      <rect x="376" y="84" width="48" height="34" rx="6" fill="var(--gold)"
        role="img" aria-label="Small gold crown ornament"/>

      <!-- origin banner -->
      <rect x="250" y="140" width="300" height="46" rx="8" fill="var(--cream)" stroke="var(--gold)" stroke-width="4"/>

      <!-- emblem circle -->
      <circle cx="400" cy="255" r="40" fill="var(--white)" stroke="var(--crest-red)" stroke-width="6"/>

      <!-- divider under name -->
      <line x1="230" y1="418" x2="570" y2="418" stroke="var(--white)" stroke-width="3"/>

      <!-- main ribbon band -->
      <rect x="100" y="588" width="600" height="80" fill="var(--label-navy)" stroke="var(--gold)" stroke-width="5"/>
      <rect x="112" y="598" width="576" height="60" fill="none" stroke="var(--gold-light)" stroke-width="2"/>

      <!-- product type tag -->
      <rect x="278" y="678" width="244" height="34" rx="4" fill="var(--label-navy)" stroke="var(--gold)" stroke-width="3"/>
    </svg>

    <div class="label-text origin-banner">MADE IN ESTONIA</div>
    <div class="label-text brand-name">HALVIK</div>
    <div class="label-text brand-sub">DISTILLERY</div>
    <div class="label-text established"><span class="dot">•</span> EST 2023 <span class="dot">•</span></div>
    <div class="label-text company-name">LOREM IPSUM CO.</div>
    <div class="label-text product-type">PREMIUM RUM</div>
    <div class="label-text volume">700 ML</div>
  </div>
</body>
</html>
```